KTR Business Cards

We require business cards for our business. We would like a matte black back to the card, with our logo centred in the middle. The front side of the card is open to design.

Target Market(s)

Clients looking for legal services (professional)

Industry/Entity Type

Legal

Contact Information for Business Card

Dario Velkenor
Partner
Mobile: 0471 386 524
Email: dario@ktrlaw.co
Website: www.ktrlaw.co
Level 3, 118 Pembury Street
Sydney NSW 2000

Font styles to use
Other font styles liked:
• Avenir

Colors
f04a50
ffffff
1b1b1b

Requirements
Must have
• Black back with logo included in the centre of the card.
• Our font is Avenir.

```html
<!DOCTYPE html>
<html lang="en">
<head>
<meta charset="utf-8">
<title>Koren Tavlin Legal — Business Cards</title>
<link rel="stylesheet" href="https://fonts.googleapis.com/css2?family=Mulish:wght@400;600;700&display=swap">
<style>
  :root {
    --brand-red: #f04a50;
    --deep-red: #c8234a;
    --white: #ffffff;
    --card-black: #1b1b1b;
    --card-charcoal: #222325;
    --stage: #2a2a2d;
    --muted: #d9d9d9;
    --motif-warm: #4a3434;
    --motif-grey: #4a4b4e;
  }
  * { box-sizing: border-box; margin: 0; padding: 0; }
  html, body { width: 1200px; height: 800px; overflow: hidden; }
  body {
    background: var(--stage);
    font-family: "Mulish", "Avenir", sans-serif;
    position: relative;
  }
  .card {
    position: absolute;
    width: 540px;
    height: 309px;
    background: var(--card-charcoal);
    overflow: hidden;
    box-shadow: 0 18px 40px rgba(0,0,0,.45);
  }
  .card--back { left: 40px; top: 245px; background: var(--card-black); }
  .card--front { left: 620px; top: 245px; }

  .corner-motif {
    position: absolute;
    right: 0; top: 0;
    width: 230px; height: 170px;
    background: linear-gradient(225deg, var(--motif-grey) 0%, var(--motif-warm) 45%, rgba(74,52,52,0) 90%);
    opacity: .75;
  }
  .card--front .corner-motif { opacity: .45; }

  .wordmark {
    position: absolute;
    display: flex;
    align-items: center;
    gap: 12px;
    color: var(--white);
    font-weight: 700;
    text-transform: uppercase;
    letter-spacing: .02em;
  }
  .wordmark__square {
    width: 30px; height: 30px;
    background: var(--white);
    flex: none;
  }
  .wordmark__name { font-size: 21px; line-height: 1.02; }
  .card--back .wordmark { left: 50%; top: 50%; transform: translate(-50%, -50%); }
  .card--front .wordmark { left: 54px; top: 62px; }
  .card--front .wordmark__name { font-size: 19px; }
  .card--front .wordmark__square { width: 26px; height: 26px; }

  .rule {
    position: absolute;
    left: 40px; right: 30px; top: 178px;
    height: 1.5px;
    background: var(--deep-red);
  }
  .address {
    position: absolute;
    right: 34px; top: 134px;
    color: var(--muted);
    font-size: 12px;
    line-height: 1.4;
    text-align: left;
  }
  .person { position: absolute; left: 40px; top: 190px; }
  .person__name {
    color: var(--deep-red);
    font-weight: 700;
    font-size: 16px;
    text-transform: uppercase;
    letter-spacing: .02em;
  }
  .person__role { color: var(--muted); font-size: 12.5px; margin-top: 1px; }
  .contact {
    list-style: none;
    position: absolute;
    left: 40px; top: 236px;
    color: var(--muted);
    font-size: 12.5px;
    line-height: 1.55;
  }
  .contact li { display: flex; align-items: center; gap: 9px; }
  .contact svg { width: 11px; height: 11px; flex: none; }
</style>
</head>
<body>

  <section class="card card--back" aria-label="Card back">
    <div class="corner-motif" role="img" aria-label="Decorative block pattern in warm brown and grey tones"></div>
    <div class="wordmark">
      <span class="wordmark__square"></span>
      <span class="wordmark__name">Koren<br>Tavlin<br>Legal</span>
    </div>
  </section>

  <section class="card card--front" aria-label="Card front">
    <div class="corner-motif" role="img" aria-label="Decorative block pattern in warm brown and grey tones"></div>
    <div class="wordmark">
      <span class="wordmark__square"></span>
      <span class="wordmark__name">Koren<br>Tavlin<br>Legal</span>
    </div>

    <p class="address">Level 3, 118 Pembury Street<br>Sydney NSW 2000</p>
    <div class="rule"></div>

    <div class="person">
      <p class="person__name">Dario Velkenor</p>
      <p class="person__role">Partner</p>
    </div>

    <ul class="contact">
      <li>
        <svg viewBox="0 0 12 12" aria-hidden="true"><rect x="1" y="1" width="10" height="10" fill="none" stroke="var(--deep-red)" stroke-width="1.6"/></svg>
        0471 386 524
      </li>
      <li>
        <svg viewBox="0 0 12 12" aria-hidden="true"><rect x="0.5" y="2" width="11" height="8" fill="var(--deep-red)"/><path d="M0.5 2.5 6 6.5 11.5 2.5" fill="none" stroke="var(--card-charcoal)" stroke-width="1"/></svg>
        dario@ktrlaw.co
      </li>
      <li>
        <svg viewBox="0 0 12 12" aria-hidden="true"><circle cx="6" cy="6" r="5.5" fill="var(--deep-red)"/></svg>
        www.ktrlaw.co
      </li>
    </ul>
  </section>

</body>
</html>
```